Website Design für Reinigungsunternehmen
Zielgruppe
Wir sind ein Reinigungsunternehmen, dass seit 2014 am Markt ist.
Was machen wir:
Das Angebot besteht darin, Räume nach dem IFSG (Infektionsschutzgesetz) und den Richtlinien des Werner Lasko Instituts mit ausgewählten Verfahren keimfrei zu bekommen.
Hygiene und prophylaktische Desinfektion sind für die Nutzung stark frequentierter Räume und Oberflächen gerade jetzt essentiell, denn die Ausbreitung von Viren und Bakterien kann auch durch präventive Maßnahmen eingedämmt werden.
Das Angebot ist, mit speziellen Reinigungsverfahren in Kombination mit Kaltverneblung ,die Räume fast vollständig von Keimen, Viren und Bakterien zu befreien.
So ist auch die Desinfektion von schwer zugänglichen Stellen und Gegenständen gewährleistet. Die eingesetzte Kaltnebeltechnologie wirkt in Verbindung mit Wasserstoffperoxid in verschiedenen Konzentrationen sowohl bakterizid, viruzid als auch fungizid. Wasserstoffperoxid wird rückstandsfrei abgebaut. Nach einer Einwirkzeit kann der behandelte, desinfizierte Raum sofort mechanisch gelüftet werden – ohne Material oder Umweltschäden zu riskieren.
Hier ein kurzes und erklärendes Video: https://klipvid.example/Qx7tmRwPaen
Aufgabenstellung
Die Website Soll maximal 3 Seiten haben.. Home (bzw. was wir machen..) Über uns (wer wir sind..) und Kontakt (-daten.
Ich möchte relativ kurz und knapp zum Thema kommen. Wenig Text, nur das wesentliche auf den Punkt gebracht - dafür ein ansprechendes professionelles Design. Bitte keine Bilder mit Gebäude, Reiniger etc. - dafür andere kreative Assoziationen einbringen.

```html
<!DOCTYPE html>
<html lang="de">
<head>
<meta charset="utf-8">
<title>halvex Gebäudereinigung – Innovative Hygienekonzepte</title>
<link rel="stylesheet" href="https://fonts.googleapis.com/css2?family=Montserrat:ital,wght@0,400;0,500;0,600;0,700;0,800;1,400&display=swap">
<style>
:root{
  --navy:#1f3159;
  --sky:#6aa8d4;
  --sky-light:#cfe3f2;
  --white:#ffffff;
  --footer-bg:#efeff0;
  --field-bg:#e1e1e3;
  --text:#1f3159;
}
*{margin:0;padding:0;box-sizing:border-box}
html,body{width:1190px;height:1200px;overflow:hidden}
body{position:relative;background:var(--white);font-family:"Montserrat",sans-serif;color:var(--text)}
.abs{position:absolute}

/* hero */
.hero{position:absolute;left:0;top:0;width:1190px;height:565px;background:var(--white)}
.splash{position:absolute;background:linear-gradient(160deg,rgba(207,227,242,.9),rgba(106,168,212,.55) 55%,rgba(220,235,246,.8));border-radius:48% 52% 40% 60% / 30% 40% 60% 70%}
.splash-left{left:168px;top:0;width:180px;height:530px;transform:rotate(-6deg)}
.splash-right{left:845px;top:100px;width:175px;height:465px;transform:rotate(8deg)}

.nav{position:absolute;top:25px;left:0;width:1190px;height:30px}
.nav a{position:absolute;top:0;height:30px;line-height:30px;font-size:11.5px;font-weight:600;color:var(--navy);text-decoration:none;letter-spacing:.02em;transform:translateX(-50%)}
.nav a.active{border:1.5px solid var(--sky);border-radius:16px;width:74px;text-align:center;color:var(--sky);font-weight:700;line-height:27px}

.brand{position:absolute;display:flex;align-items:center}
.brand-dot{border-radius:50%;background:var(--navy)}
.brand-name{font-weight:600;color:var(--navy);letter-spacing:-.01em}
.hero-brand{top:142px;left:50%;transform:translateX(-50%);gap:12px}
.hero-brand .brand-dot{width:46px;height:46px;background:var(--sky)}
.hero-brand .brand-name{font-size:54px;line-height:58px}
.hero-brand small{display:block;font-size:7px;letter-spacing:.18em;text-align:right;margin-top:-6px;font-weight:500}

.headline{position:absolute;top:240px;left:0;width:1190px;text-align:center}
.headline-main{font-size:65px;font-weight:800;line-height:56px;color:var(--navy);letter-spacing:-.01em}
.headline-sub{font-size:40px;font-weight:800;line-height:42px;color:var(--sky)}
.lead{position:absolute;top:370px;left:0;width:1190px;text-align:center;font-size:13.6px;font-weight:500;line-height:16.5px;color:var(--navy);letter-spacing:.01em}
.lead strong{color:var(--sky);font-weight:700}
.btn{position:absolute;left:539px;top:464px;width:111px;height:31px;border-radius:16px;background:var(--sky);color:var(--white);font-size:11px;font-weight:700;text-align:center;line-height:31px;box-shadow:0 3px 4px rgba(31,49,89,.25);letter-spacing:.02em}

/* services */
.services{position:absolute;left:0;top:565px;width:1190px;height:448px;background:var(--navy)}
.card{position:absolute;top:109px;width:229px;height:228px;border-radius:30px;background:var(--sky);color:var(--white);box-shadow:0 4px 10px rgba(0,0,0,.2)}
.card.light{background:var(--white);color:var(--sky)}
.card-icon{position:absolute;left:27px;top:22px;width:39px;height:39px}
.card-title{position:absolute;left:27px;top:77px;width:190px;font-size:18px;font-weight:700;line-height:15.5px}
.card-text{position:absolute;left:28px;width:180px;font-size:9px;line-height:10.5px;font-weight:400}
.card-link{position:absolute;left:28px;top:185px;font-size:11px;font-weight:700;display:flex;align-items:center;gap:10px;letter-spacing:.02em}

/* footer */
.footer{position:absolute;left:0;top:1013px;width:1190px;height:187px;background:var(--footer-bg)}
.footer-brand{left:233px;top:30px;gap:5px}
.footer-brand .brand-dot{width:20px;height:20px;background:var(--sky)}
.footer-brand .brand-name{font-size:24px;line-height:26px}
.company{left:233px;top:76px;font-size:9px;line-height:10.5px}
.company b{color:var(--sky);font-weight:700}
.col-title{font-size:9px;font-weight:700;letter-spacing:.02em}
.col-list{list-style:none;font-size:9.5px}
.col-list li{height:20.5px}
.contact-list li{display:flex;gap:6px;align-items:center}
.field{left:790px;top:54px;width:168px;height:32px;border-radius:6px;background:var(--field-bg);font-size:9.5px;font-style:italic;color:#8e96a8;padding-left:11px;line-height:32px}
.field svg{position:absolute;right:9px;top:11px}
.fine{font-size:7.8px;line-height:8px}
.rule{left:233px;top:156px;width:725px;height:1px;background:#d3d4d8}
.copyright{left:0;top:168px;width:1190px;text-align:center;font-size:7.8px;font-weight:500}
.copyright b{color:var(--sky)}
</style>
</head>
<body>

<section class="hero">
  <div class="splash splash-left" role="img" aria-label="Wasserspritzer, der von oben links ins Bild fließt"></div>
  <div class="splash splash-right" role="img" aria-label="Aufsteigender Wasserspritzer mit Tropfen am rechten Rand"></div>

  <nav class="nav">
    <a class="active" href="#" style="left:474px">HOME</a>
    <a href="#" style="left:581px">LEISTUNGEN</a>
    <a href="#" style="left:706px">KONTAKT</a>
  </nav>

  <div class="brand hero-brand">
    <span class="brand-dot"></span>
    <span class="brand-name">halvex<small>GEBÄUDEREINIGUNG</small></span>
  </div>

  <h1 class="headline">
    <div class="headline-main">INNOVATIVE</div>
    <div class="headline-sub">HYGIENEKONZEPTE</div>
  </h1>

  <p class="lead">Wir schließen Reinigungslücken und befreien<br>Ihre Räumlichkeiten zu <strong>99,9 %</strong> von<br><strong>Viren, Bakterien und Keimen</strong></p>

  <div class="btn">LERN MEHR</div>
</section>

<section class="services">
  <article class="card" style="left:233px">
    <svg class="card-icon" viewBox="0 0 40 40" fill="none" stroke="currentColor" stroke-width="2.4">
      <path d="M33 12A16 16 0 1 0 35 24"/><path d="M27 10l6 2 1-6" stroke-linejoin="round"/>
      <path d="M20 11c-3 5-6 8-6 12a6 6 0 0 0 12 0c0-4-3-7-6-12z" fill="currentColor" stroke="none"/>
    </svg>
    <h2 class="card-title">Flächen- und Raumdesinfektion gem. IFSG § 17</h2>
    <p class="card-text" style="top:139px">Lorem ipsum dolor sit amet, consectetur adipiscing elit</p>
    <div class="card-link">LERN MEHR
      <svg width="16" height="12" viewBox="0 0 16 12" fill="none" stroke="currentColor" stroke-width="2.4" stroke-linecap="round" stroke-linejoin="round"><path d="M1 6h13M9 1l5 5-5 5"/></svg>
    </div>
  </article>

  <article class="card light" style="left:481px">
    <svg class="card-icon" viewBox="0 0 40 40" fill="none" stroke="currentColor" stroke-width="2.4">
      <path d="M33 12A16 16 0 1 0 35 24"/><path d="M27 10l6 2 1-6" stroke-linejoin="round"/>
      <path d="M20 11c-3 5-6 8-6 12a6 6 0 0 0 12 0c0-4-3-7-6-12z" fill="currentColor" stroke="none"/>
    </svg>
    <h2 class="card-title">WLI gelistete und geprüfte Verfahren</h2>
    <p class="card-text" style="top:136px">Lorem ipsum dolor sit amet, consectetur adipiscing elit</p>
    <div class="card-link">LERN MEHR
      <svg width="16" height="12" viewBox="0 0 16 12" fill="none" stroke="currentColor" stroke-width="2.4" stroke-linecap="round" stroke-linejoin="round"><path d="M1 6h13M9 1l5 5-5 5"/></svg>
    </div>
  </article>

  <article class="card" style="left:729px">
    <svg class="card-icon" viewBox="0 0 40 40" fill="none" stroke="currentColor" stroke-width="2.4">
      <path d="M33 12A16 16 0 1 0 35 24"/><path d="M27 10l6 2 1-6" stroke-linejoin="round"/>
      <path d="M20 11c-3 5-6 8-6 12a6 6 0 0 0 12 0c0-4-3-7-6-12z" fill="currentColor" stroke="none"/>
    </svg>
    <h2 class="card-title">Staatlich geprüfte Desinfektoren</h2>
    <p class="card-text" style="top:136px">Lorem ipsum dolor sit amet, consectetur adipiscing elit</p>
    <div class="card-link">LERN MEHR
      <svg width="16" height="12" viewBox="0 0 16 12" fill="none" stroke="currentColor" stroke-width="2.4" stroke-linecap="round" stroke-linejoin="round"><path d="M1 6h13M9 1l5 5-5 5"/></svg>
    </div>
  </article>
</section>

<footer class="footer">
  <div class="brand footer-brand abs">
    <span class="brand-dot"></span>
    <span class="brand-name">halvex</span>
  </div>
  <p class="company abs"><b>HALVEX GROUP</b><br>Gebäudereinigung &amp; Hygienekonzepte<br>Lindenweg 4<br>93199 Musterfeld</p>

  <div class="abs" style="left:480px;top:38px">
    <h3 class="col-title">QUICK LINKS</h3>
    <ul class="col-list" style="margin-top:16px"><li>HOME</li><li>LEISTUNGEN</li><li>KONTAKT</li></ul>
  </div>

  <div class="abs" style="left:604px;top:38px">
    <h3 class="col-title">KONTAKT UNS</h3>
    <ul class="col-list contact-list" style="margin-top:16px">
      <li><svg width="11" height="11" viewBox="0 0 12 12" fill="#6aa8d4"><path d="M2.5 0.5l2 2.5-1.2 1.5c.7 1.6 2.1 3 3.7 3.7L8.5 7l2.5 2-1 2.2C5 11 1 7 0.8 1.5z"/></svg>09400 / 512 340 10</li>
      <li><svg width="11" height="11" viewBox="0 0 12 12" fill="#6aa8d4"><rect x="3" y="0.5" width="6" height="4" rx=".5"/><rect x="1" y="4.5" width="10" height="5" rx="1"/><rect x="3" y="8" width="6" height="3.5"/></svg>09400 / 512 340 19</li>
      <li><svg width="11" height="9" viewBox="0 0 12 9" fill="#6aa8d4"><path d="M0 0h12v9H0z"/><path d="M0 0l6 5 6-5" fill="none" stroke="#efeff0" stroke-width="1"/></svg>mail@halvex-group.de</li>
    </ul>
  </div>

  <h3 class="col-title abs" style="left:790px;top:38px">NEWSLETTER</h3>
  <div class="field abs">Email address
    <svg width="12" height="9" viewBox="0 0 12 9" fill="#6aa8d4"><path d="M0 0h12v9H0z"/><path d="M0 0l6 5 6-5" fill="none" stroke="#e1e1e3" stroke-width="1"/></svg>
  </div>
  <p class="fine abs" style="left:790px;top:97px;width:170px">Lorem ipsum dolor sit amet, consectetur adipiscing elit</p>

  <div class="rule abs"></div>
  <p class="copyright abs">ALL RIGHTS RESERVED BY <b>9FENNEL</b></p>
</footer>

</body>
</html>
```